Thank you for shopping with us business card

We would like a thank you card for our rebranded business. We used to be "Brindle Goods" but are now "Marlow Finds. Old thank you card and new logo will be attached for reference. New thank you card does not have to be same design as old thank you card, but please use new logo.
Shopmart URL is now marlowfinds.shopmart.example
Instagram is @Marlow_Finds
Email is marlowfinds@mailbox.example
Thank you!

Contact Information for Business Card

Shopmart site, email, Instagram

```html
<!DOCTYPE html>
<html lang="en">
<head>
<meta charset="utf-8">
<title>Marlow Finds – Thank You Card</title>
<link rel="stylesheet" href="https://fonts.googleapis.com/css2?family=Inter:wght@400;700;800&family=Montserrat:wght@500;600&display=swap">
<style>
  :root {
    --backdrop: #9a9a9a;
    --card-dark: #161616;
    --card-dark-light: #3a3a3a;
    --card-light: #ffffff;
    --ink: #0d0d0d;
    --ink-soft: #444444;
    --paper-text: #ffffff;
  }
  * { margin: 0; padding: 0; box-sizing: border-box; }
  html, body { width: 1200px; height: 588px; overflow: hidden; }
  body {
    background: var(--backdrop);
    position: relative;
    font-family: "Inter", sans-serif;
  }
  .card {
    position: absolute;
    width: 488px;
    height: 287px;
  }
  /* Front */
  .card-front {
    left: 87px; top: 141px;
    background: var(--card-dark);
    overflow: hidden;
  }
  .front-pattern {
    position: absolute; inset: 0;
    background: linear-gradient(90deg, var(--card-dark) 0%, #1e1e1e 45%, var(--card-dark-light) 100%);
  }
  .front-lockup {
    position: absolute;
    left: 250px; top: 152px;
    display: flex; align-items: center;
    height: 59px;
  }
  .front-mark {
    width: 46px; height: 46px;
    border-radius: 50%;
    background: var(--paper-text);
  }
  .front-divider {
    width: 1px; height: 59px;
    background: var(--paper-text);
    margin: 0 16px 0 18px;
  }
  .front-name {
    font-family: "Montserrat", sans-serif;
    font-weight: 500;
    font-size: 19px;
    line-height: 25px;
    color: var(--paper-text);
    text-transform: uppercase;
  }
  /* Back */
  .card-back {
    left: 622px; top: 143px;
    background: var(--card-light);
  }
  .back-mark {
    position: absolute;
    left: 57px; top: 78px;
    width: 74px; height: 74px;
    border-radius: 50%;
    background: var(--ink);
  }
  .back-name {
    position: absolute;
    left: 0; width: 188px; top: 184px;
    text-align: center;
    font-family: "Montserrat", sans-serif;
    font-weight: 600;
    font-size: 13.5px;
    color: var(--ink);
    text-transform: uppercase;
  }
  .back-divider {
    position: absolute;
    left: 190px; top: 76px;
    width: 1px; height: 122px;
    background: var(--ink);
  }
  .thanks-heading {
    position: absolute;
    left: 211px; top: 72px;
    font-weight: 800;
    font-size: 24px;
    line-height: 28px;
    color: var(--ink);
    text-transform: uppercase;
    white-space: nowrap;
  }
  .thanks-message {
    position: absolute;
    left: 211px; top: 143px;
    font-size: 13.5px;
    line-height: 20px;
    color: var(--ink-soft);
    white-space: nowrap;
  }
  .contact-row {
    position: absolute;
    left: 19px; top: 255px;
    display: flex; align-items: center; gap: 9px;
    font-size: 10.5px;
    color: var(--ink-soft);
    white-space: nowrap;
  }
  .contact-item { display: flex; align-items: center; gap: 3px; }
  .icon-dot { width: 9px; height: 9px; border-radius: 50%; background: var(--ink); }
  .icon-square { width: 8px; height: 8px; border: 1.3px solid var(--ink); border-radius: 2px; }
  .icon-mail { width: 10px; height: 8px; display: block; }
</style>
</head>
<body>
  <section class="card card-front">
    <div class="front-pattern" role="img" aria-label="Repeating brand symbol pattern in tonal black fading to dark grey"></div>
    <div class="front-lockup">
      <div class="front-mark"></div>
      <div class="front-divider"></div>
      <p class="front-name">Marlow<br>Finds</p>
    </div>
  </section>

  <section class="card card-back">
    <div class="back-mark"></div>
    <p class="back-name">Marlow Finds</p>
    <div class="back-divider"></div>
    <h1 class="thanks-heading">Thank you for<br>your purchase</h1>
    <p class="thanks-message">Your Purchase Made my day and I<br>hope this package brightness yours.<br>Please come back and leave a review!</p>
    <div class="contact-row">
      <span class="contact-item"><span class="icon-dot"></span>marlowfinds.shopmart.example</span>
      <span class="contact-item"><span class="icon-square"></span>@Marlow_Finds</span>
      <span class="contact-item">
        <svg class="icon-mail" viewBox="0 0 10 8" aria-hidden="true">
          <rect x="0" y="0" width="10" height="8" fill="#0d0d0d"/>
          <path d="M0.5 0.8 L5 4.5 L9.5 0.8" fill="none" stroke="#fff" stroke-width="1"/>
        </svg>marlowfinds@mailbox.example</span>
    </div>
  </section>
</body>
</html>
```